Wordpress and Elementor Pro website

We need a Wordpress/Elementor Pro design for our website. We already have a logo design and installed Wordpress. We have some ideas concerning the design, and we will share two websites. Both the design and content placement we like about these websites. We would like to see designs that use the color Purple (the same as the logo color), white and black. We provide these services: SEO optimization, SEO copywriting and online campaigns. We will provide a list of the page's we would like to see in the design.

Target Market(s)

Entrepreneurs, business owners. Companies who would like to expand online with texts and SEO.

Industry/Entity Type

Digital Marketing

Coding

Coded - Design and coding required

Number of Pages Required

5+ page

Font styles to use
Sans Serif

Colors
886aae
fffefd
0355a3

Requirements
Must have
• Single pages and singel posts of Elementor so I can create new pages and blog posts in the future.

```html
<!DOCTYPE html>
<html lang="nl">
<head>
<meta charset="utf-8">
<title>Groeimeester</title>
<link rel="stylesheet" href="https://fonts.googleapis.com/css2?family=Montserrat:wght@400;500;600;700;800&display=swap">
<style>
:root{
  --purple:#663399;
  --purple-dark:#4e2579;
  --ink:#1e2a38;
  --text:#3a4350;
  --band:#f5f9fc;
  --footer:#1b2a38;
  --grey:#d8d8d8;
  --white:#ffffff;
}
*{margin:0;padding:0;box-sizing:border-box}
html,body{width:1200px;height:3499px;overflow:hidden;background:var(--white)}
body{position:relative;font-family:"Montserrat",sans-serif;color:var(--ink)}
.abs{position:absolute}

/* header */
.brand{left:234px;top:28px;width:170px;text-align:center}
.brand-mark{width:44px;height:44px;border:3px solid var(--purple);border-radius:4px;margin:0 auto 12px}
.brand-name{font-size:25px;font-weight:500;color:var(--purple);letter-spacing:1px}
.nav{top:55px;left:484px;display:flex;gap:0;font-size:12px;font-weight:700;letter-spacing:1px}
.nav span{display:block}
.nav .active{color:var(--purple)}
.nav .sep{width:1px;height:14px;background:#c9c9c9;margin-top:0}
.caret{display:inline-block;border:4px solid transparent;border-top-color:var(--purple);margin-left:4px;vertical-align:-2px}

/* services */
.service{top:190px;width:236px}
.service-icon{width:56px;height:56px;border-radius:12px;background:linear-gradient(135deg,#8fb4e6,#f4cf5a)}
.service h3{font-size:12px;font-weight:700;letter-spacing:1px;margin-top:20px}
.service p{font-size:10.5px;line-height:17.5px;margin-top:14px;color:var(--text)}

.claim{left:234px;top:452px;font-size:41px;font-weight:800;line-height:45px;letter-spacing:3.5px;text-transform:uppercase}

/* clients */
.clients{left:0;top:676px;width:1200px;height:345px;background:var(--band)}
.client{width:150px;text-align:center;font-size:19px;font-weight:700;color:var(--ink)}

/* about */
.about-band{left:235px;top:1107px;width:325px;height:340px;background:var(--purple)}
.about-name{left:235px;top:1107px;width:72px;height:340px;display:flex;align-items:center;justify-content:center}
.about-name span{transform:rotate(-90deg);white-space:nowrap;color:var(--white);font-size:23px;font-weight:700;letter-spacing:2px}
.about-photo{left:301px;top:1124px;width:283px;height:340px;background:linear-gradient(160deg,#c7c3bd,#8a7b6c 55%,#3d3b3e)}
.about-text{left:654px;top:1116px;width:315px}
.about-text h2{font-size:26px;font-weight:600}
.about-text .lead{font-size:13.5px;font-weight:700;line-height:20px;margin-top:18px;text-align:justify}
.about-text p{font-size:10.5px;line-height:20px;margin-top:16px;color:var(--text);text-align:justify}

/* pillars */
.pillar{width:232px;height:289px;border:1px solid #e4e4e4;background:var(--white);text-align:center;padding:30px 22px 0;box-shadow:0 1px 3px rgba(0,0,0,.04)}
.pillar-icon{width:70px;height:76px;margin:0 auto;border-radius:50% 50% 8px 8px;background:linear-gradient(135deg,#2b2b35 40%,var(--purple))}
.pillar h3{font-size:27px;font-weight:600;margin-top:16px}
.pillar p{font-size:10.5px;line-height:20px;margin-top:16px;color:var(--text)}

/* process */
.process{left:0;top:2040px;width:1200px;height:1197px;background:var(--purple)}
.wave{left:0;top:1900px}
.hub{left:546px;top:2123px;width:108px;height:108px;border-radius:50%;background:var(--grey);display:flex;align-items:center;justify-content:center}
.hub div{width:90px;height:90px;border-radius:50%;background:var(--white);display:flex;align-items:center;justify-content:center;font-size:10px;font-weight:600;color:var(--purple)}
.axis{left:599px;top:2231px;height:897px;border-left:1px dashed rgba(255,255,255,.6)}
.col-head{top:2260px;font-size:16px;font-weight:600;color:var(--white)}
.step-label{width:200px;text-align:right;font-size:12px;font-weight:600;line-height:14px;color:var(--white)}
.step-icon{width:66px;height:66px;border-radius:50%;background:var(--white);display:flex;align-items:center;justify-content:center}
.step-icon i{display:block;width:32px;height:32px;border-radius:5px;background:linear-gradient(135deg,#f2c94c,#3b4a8c)}
.link{height:1px;background:rgba(255,255,255,.7)}
.node{width:12px;height:12px;border-radius:50%;background:var(--white);border:2px solid #cfc3e0}
.req{left:661px;width:204px;background:var(--white);padding:10px 12px;font-size:9.5px;line-height:12px;color:var(--ink)}
.req p+p{margin-top:4px}
.more{left:528px;top:3128px;width:145px;height:36px;border-radius:18px;background:var(--white);color:var(--ink);font-size:12px;font-weight:600;letter-spacing:1px;display:flex;align-items:center;justify-content:center}

/* footer */
.footer{left:0;top:3237px;width:1200px;height:262px;background:var(--footer);color:var(--white)}
.footer-col{top:68px;font-size:11px;font-weight:500;line-height:26px}
.copyright{left:0;top:214px;width:1200px;text-align:center;font-size:10px;color:#c9ced6}
</style>
</head>
<body>

<header>
  <div class="abs brand"><div class="brand-mark"></div><div class="brand-name">Groeimeester</div></div>
  <nav class="abs nav">
    <span class="active" style="margin-right:32px">HOME</span>
    <span style="margin-right:27px">SERVICES</span>
    <span style="margin-right:27px">CASES</span>
    <span style="margin-right:27px">ABOUT US</span>
    <span style="margin-right:18px">CONTACT</span>
    <span class="sep" style="margin-right:18px"></span>
    <span>EN<i class="caret"></i></span>
  </nav>
</header>

<section>
  <div class="abs service" style="left:234px">
    <div class="service-icon" role="img" aria-label="Icon: gear with document for SEO copywriting"></div>
    <h3>SEO COPYWRITING</h3>
    <p>Lorem ipsum dolor sit amet, consectetur adipiscing elit. In quam lorem, porttitor et varius sit amet, placerat id elit. Curabitur rutrum ante vel turpis tincidunt, id elementum libero sodales.</p>
  </div>
  <div class="abs service" style="left:484px">
    <div class="service-icon" role="img" aria-label="Icon: hand on screen for search engine optimization"></div>
    <h3>SEARCH ENGINE OPTIMIZATION</h3>
    <p>Lorem ipsum dolor sit amet, consectetur adipiscing elit. In quam lorem, porttitor et varius sit amet, placerat id elit. Curabitur rutrum ante vel turpis tincidunt, id elementum libero sodales.</p>
  </div>
  <div class="abs service" style="left:734px">
    <div class="service-icon" role="img" aria-label="Icon: globe with megaphone for online campaigns"></div>
    <h3>ONLINE CAMPAIGNS</h3>
    <p>Lorem ipsum dolor sit amet, consectetur adipiscing elit. In quam lorem, porttitor et varius sit amet, placerat id elit. Curabitur rutrum ante vel turpis tincidunt, id elementum libero sodales.</p>
  </div>
  <h1 class="abs claim">Omdat online groeien in<br>omzet en winst een<br>specialisme is.</h1>
</section>

<section class="abs clients">
  <div class="abs client" style="left:213px;top:117px">Northwell Aid</div>
  <div class="abs client" style="left:368px;top:117px">Lumen Care</div>
  <div class="abs client" style="left:523px;top:117px">Aspira</div>
  <div class="abs client" style="left:680px;top:117px">Civic Health</div>
  <div class="abs client" style="left:836px;top:117px">Heartmart</div>
  <div class="abs client" style="left:213px;top:208px">Ridge Tech</div>
  <div class="abs client" style="left:368px;top:208px">Sprout &amp; Co</div>
  <div class="abs client" style="left:523px;top:208px">Prime Ledger</div>
  <div class="abs client" style="left:680px;top:208px">Veyra Medical</div>
  <div class="abs client" style="left:836px;top:208px">Easely</div>
</section>

<section>
  <div class="abs about-band"></div>
  <div class="abs about-name"><span>DAAN VERHOEF</span></div>
  <div class="abs about-photo" role="img" aria-label="Photo: consultant in a suit at a desk with laptop and coffee cup"></div>
  <div class="abs about-text">
    <h2>About Us</h2>
    <p class="lead">Etiam ut sapien enim. Etiam facilisis dictum iaculis. Suspendisse sollicitudin sem quis dui vulputate sagittis.</p>
    <p>Lorem ipsum dolor sit amet, consectetur adipiscing elit. In quam lorem, porttitor et varius sit amet, placerat id elit. Curabitur rutrum ante vel turpis tincidunt, id elementum libero sodales. Vestibulum auctor massa sed lacus lobortis, vel varius dui aliquet. Duis non dapibus enim, sed condimentum sapien. Maecenas ut lacus ligula. Nam at iaculis lorem. In hac habitasse platea dictumst. Aliquam erat volutpat.</p>
    <p style="margin-top:18px">Praesent interdum fringilla velit, nec dapibus nulla dictum vel. Nam vel efficitur felis.</p>
  </div>
</section>

<section>
  <div class="abs pillar" style="left:234px;top:1547px">
    <div class="pillar-icon" role="img" aria-label="Icon: light bulb"></div>
    <h3>Strategy</h3>
    <p>Etiam ut sapien enim. Etiam facilisis dictum iaculis. Suspendisse sollicitudin sem quis dui vulputate sagittis. Vivamus quis nibh quis</p>
  </div>
  <div class="abs pillar" style="left:484px;top:1578px">
    <div class="pillar-icon" role="img" aria-label="Icon: people network with globe"></div>
    <h3>Traffic</h3>
    <p>Etiam ut sapien enim. Etiam facilisis dictum iaculis. Suspendisse sollicitudin sem quis dui vulputate sagittis. Vivamus quis nibh quis</p>
  </div>
  <div class="abs pillar" style="left:734px;top:1547px">
    <div class="pillar-icon" role="img" aria-label="Icon: bar chart with pie"></div>
    <h3>Conversion</h3>
    <p>Etiam ut sapien enim. Etiam facilisis dictum iaculis. Suspendisse sollicitudin sem quis dui vulputate sagittis. Vivamus quis nibh quis</p>
  </div>
</section>

<svg class="abs wave" width="1200" height="160" viewBox="0 0 1200 160" aria-hidden="true">
  <path d="M0 90 C150 55 260 18 380 22 C560 28 700 150 860 140 C1000 130 1100 70 1200 50 L1200 160 L0 160Z" fill="#d8d8d8"/>
  <path d="M0 128 C150 100 260 72 380 74 C560 80 700 170 860 158 C1000 148 1100 90 1200 70 L1200 160 L0 160Z" fill="#4e2579"/>
  <path d="M0 136 C150 108 260 80 380 82 C560 88 700 178 860 166 C1000 156 1100 98 1200 78 L1200 160 L0 160Z" fill="#663399"/>
</svg>

<section class="abs process">
  <div class="abs axis" style="top:191px"></div>
</section>
<div class="abs hub"><div>Groeimeester</div></div>
<div class="abs col-head" style="left:438px">Onderdelen</div>
<div class="abs col-head" style="left:661px">Vereisten</div>

<!-- row 1 -->
<div class="abs step-label" style="left:257px;top:2327px">Productpagina's of<br>diensten</div>
<div class="abs link" style="left:540px;top:2338px;width:121px"></div>
<div class="abs step-icon" style="left:473px;top:2305px"><i></i></div>
<div class="abs node" style="left:594px;top:2332px"></div>
<div class="abs req" style="top:2311px"><p>Kolommen of alinea's met subkopjes. Per product de juiste productspecificaties.</p></div>

<!-- row 2 -->
<div class="abs step-label" style="left:257px;top:2433px">Blog</div>
<div class="abs link" style="left:540px;top:2439px;width:121px"></div>
<div class="abs step-icon" style="left:473px;top:2406px"><i></i></div>
<div class="abs node" style="left:594px;top:2433px"></div>
<div class="abs req" style="top:2411px"><p>Helpt enorm om verbinding te leggen met de doelgroep en bezoekers vanuit Google te trekken. Alleen inzetten als het blog structureel wordt bijgehouden en gereageerd op reacties</p></div>

<!-- row 3 -->
<div class="abs step-label" style="left:257px;top:2567px">Teksten</div>
<div class="abs link" style="left:540px;top:2573px;width:121px"></div>
<div class="abs step-icon" style="left:473px;top:2540px"><i></i></div>
<div class="abs node" style="left:594px;top:2567px"></div>
<div class="abs req" style="top:2546px">
  <p>Goed geschreven. Taal, stijl, interpunctie, zinslengte en signaalwoorden. Klantgericht: interessant om te lezen en relevant. Pas opsommingen toe waar mogelijk.</p>
  <p>Actiegericht: Schrijf teksten gericht op het doel dat je hebt met je bezoeker. Help je bezoeker om het door hem gezochte product te vinden en in contact te komen met de juiste medewerker.</p>
  <p>CTA's: Call To Actions. Voorbeelden: demo-aanvraag, brochure aanvragen, webinar-inschrijving, ebook, whitepaper etc.</p>
</div>

<!-- row 4 -->
<div class="abs step-label" style="left:257px;top:2826px">Aantal woorden</div>
<div class="abs link" style="left:540px;top:2832px;width:121px"></div>
<div class="abs step-icon" style="left:473px;top:2799px"><i></i></div>
<div class="abs node" style="left:594px;top:2826px"></div>
<div class="abs req" style="top:2816px;padding:9px 12px"><p>Minimaal 500 per pagina</p></div>

<!-- row 5 -->
<div class="abs step-label" style="left:257px;top:2933px">Zoekwoorden</div>
<div class="abs link" style="left:540px;top:2939px;width:121px"></div>
<div class="abs step-icon" style="left:473px;top:2906px"><i></i></div>
<div class="abs node" style="left:594px;top:2933px"></div>
<div class="abs req" style="top:2911px">
  <p>LSI zoekwoorden (bijv. naast "hondenvoer kopen" bijvoorbeeld "puppievoer kopen"). De winst zit vaak in het scoren op langere zoekwoorden, waar minder op wordt geconcurreerd.</p>
  <p>Belangrijkste zoekwoord in H1 en H2 titels en eerste alinea.</p>
</div>

<div class="abs more">LOAD MORE</div>

<footer class="abs footer">
  <div class="abs footer-col" style="left:234px">Cookie Policy<br>Disclaimer<br>Privacy Policy</div>
  <div class="abs footer-col" style="left:434px">VAT No.: 80417735<br>CoC No.: 6620184457</div>
  <div class="abs footer-col" style="left:666px">+31 (0)20 555 0142<br>info@groeimeester.nl</div>
  <div class="abs copyright">Copyright © 2020 Groeimeester. All Rights Reserved.</div>
</footer>

</body>
</html>
```